Brochure Needed for Concert Series

Color, glossy, tri-fold brochure for exciting concert series. Should be attractive design to make people open, and donate!
Requirements
Should not have
- Lots of extraneous music symbols.

```html
<!DOCTYPE html>
<html lang="en">
<head>
<meta charset="utf-8">
<title>Music at St. Alder's – Concert Series</title>
<link href="https://fonts.googleapis.com/css2?family=Didact+Gothic&family=Quicksand:wght@400&display=swap" rel="stylesheet">
<style>
  :root {
    --red: #e8202a;
    --charcoal: #3d3d3f;
    --black: #111214;
    --white: #ffffff;
    --navy-a: #27465f;
    --navy-b: #0d1822;
  }
  html, body { margin: 0; padding: 0; width: 1200px; height: 1200px; overflow: hidden; background: var(--white); }
  .stage { position: absolute; left: 0; top: 0; width: 1500px; height: 1500px; transform: scale(0.8); transform-origin: 0 0; }
  .shapes { position: absolute; left: 0; top: 0; width: 1500px; height: 1500px; }
  .txt { position: absolute; color: var(--white); font-family: "Didact Gothic", sans-serif; }
  .heading { font-size: 20.5px; line-height: 21px; text-align: center; letter-spacing: 0.3px; }
  .event-title { font-size: 16.5px; line-height: 20.5px; letter-spacing: 0.3px; }
  .blurb { position: absolute; border: 1px solid var(--white); color: var(--white); font-family: "Quicksand", sans-serif; font-size: 13.6px; line-height: 17.8px; padding: 2px 4px; box-sizing: border-box; }
  .blurb.justified { text-align: justify; }
  .extra-heading { font-size: 28px; letter-spacing: 0.5px; }
  .footer-note { font-size: 16.5px; }
</style>
</head>
<body>
<div class="stage">
  <svg class="shapes" viewBox="0 0 1500 1500" xmlns="http://www.w3.org/2000/svg">
    <defs>
      <linearGradient id="ensemble" x1="0" y1="0" x2="1" y2="1">
        <stop offset="0" stop-color="var(--navy-a)"/>
        <stop offset="1" stop-color="var(--navy-b)"/>
      </linearGradient>
      <radialGradient id="portraitWarm" cx="0.5" cy="0.45" r="0.6">
        <stop offset="0" stop-color="#8a6a5a"/><stop offset="1" stop-color="#2a2224"/>
      </radialGradient>
      <radialGradient id="portraitGrey" cx="0.5" cy="0.45" r="0.6">
        <stop offset="0" stop-color="#b9a89c"/><stop offset="1" stop-color="#6f7075"/>
      </radialGradient>
      <radialGradient id="portraitField" cx="0.5" cy="0.4" r="0.6">
        <stop offset="0" stop-color="#e6e2d6"/><stop offset="1" stop-color="#6b7452"/>
      </radialGradient>
      <radialGradient id="portraitLight" cx="0.5" cy="0.4" r="0.6">
        <stop offset="0" stop-color="#f1f1f1"/><stop offset="1" stop-color="#8d8d90"/>
      </radialGradient>
    </defs>

    <rect class="ensemble-photo" x="0" y="220" width="1000" height="1060" fill="url(#ensemble)" role="img" aria-label="Group portrait of the eight-member vocal ensemble"/>

    <polygon class="band-top" points="855,220 1095,220 998,300" fill="var(--charcoal)"/>
    <polygon class="panel-red" points="998,300 1095,220 1500,220 1500,670 1000,1085" fill="var(--red)"/>
    <polygon class="panel-charcoal" points="1000,1085 1500,670 1500,1280 960,1280 600,962 670,935" fill="var(--charcoal)"/>
    <polygon class="band-black" points="0,1025 670,935 600,962 0,1190" fill="var(--black)"/>
    <polygon class="band-red" points="0,1190 600,962 960,1280 0,1280" fill="var(--red)"/>

    <g stroke="var(--white)" stroke-width="2" fill="none" class="frame-marks">
      <polyline points="172,240 15,240 15,265"/>
      <line x1="15" y1="345" x2="15" y2="368"/><line x1="15" y1="375" x2="15" y2="395"/>
      <polyline points="1302,240 1478,240 1478,270"/>
      <line x1="1478" y1="345" x2="1478" y2="360"/><line x1="1478" y1="368" x2="1478" y2="382"/>
      <line x1="985" y1="665" x2="985" y2="685"/><line x1="985" y1="692" x2="985" y2="710"/>
      <line x1="985" y1="720" x2="985" y2="855"/>
      <polyline points="1325,1255 1478,1255 1478,1230"/>
      <line x1="1478" y1="1100" x2="1478" y2="1118"/><line x1="1478" y1="1128" x2="1478" y2="1150"/>
    </g>

    <polygon points="1122,328 1213,380 1213,485 1122,537 1031,485 1031,380" fill="url(#portraitWarm)" role="img" aria-label="Portrait of the guitarist playing a jazz guitar"/>
    <polygon points="1380,571 1471,623 1471,728 1380,780 1289,728 1289,623" fill="url(#portraitGrey)" role="img" aria-label="Portrait of the conductor and composer"/>
    <polygon points="1122,815 1213,867 1213,972 1122,1024 1031,972 1031,867" fill="url(#portraitField)" role="img" aria-label="Portrait of the clarinetist in a field"/>
    <polygon points="1372,1040 1463,1092 1463,1197 1372,1249 1281,1197 1281,1092" fill="url(#portraitLight)" role="img" aria-label="Portrait of the organist"/>
  </svg>

  <div class="txt heading" style="left:1010px; top:270px; width:480px;">“Music at St. Alder's presents four spectacular<br>Sunday afternoon concerts . . .”</div>

  <div class="txt event-title" style="left:1222px; top:343px;">Martin Ashford and Friends<br>Sunday, September 9<br>3:00pm</div>
  <div class="blurb" style="left:1222px; top:413px; width:250px; height:95px;">Join us for a fantastic afternoon of jazz, led by internationally-acclaimed guitarist and Albuquerque resident Martin Ashford.</div>

  <div class="txt event-title" style="left:1026px; top:558px;">Daniel Reeve<br>Sunday, November 11<br>3:00pm</div>
  <div class="blurb justified" style="left:1026px; top:627px; width:250px; height:166px;">Daniel Reeve is a conductor, a composer, an educator, and a founding member of the international a cappella sensation Cantus Nine. Daniel Reeve presents “Reflections,” an immersive and interactive experience featuring music made by chorus, instruments, and audience.</div>

  <div class="txt event-title" style="left:1222px; top:818px;">Murmur<br>Sunday, January 20<br>3:00pm</div>
  <div class="blurb" style="left:1222px; top:888px; width:250px; height:130px;">The groundbreaking Albuquerque musical collective presents “Sacred and Sublime,” an unforgettable program of new and old chamber works, featuring clarinetist Thomas Hale, and music by Hartwell, Verano, and Lindqvist.</div>

  <div class="txt event-title" style="left:1018px; top:1044px;">Andre Colvin<br>Sunday, February 10<br>3:00pm</div>
  <div class="blurb" style="left:1017px; top:1114px; width:250px; height:130px;">First-prize and Bach prize winner at the 2017 Northern International Organ Competition, Andre Colvin III is widely regarded as one of the leading young organists of our time. Join us for an afternoon of majestic music for the king of instruments.</div>
  <div class="txt footer-note" style="left:1020px; top:1248px;">“There is no admission charge”</div>

  <div class="txt extra-heading" style="left:33px; top:1034px;">“And one very special extra event . . .”</div>
  <div class="txt event-title" style="left:33px; top:1074px;">Cantus Nine<br>Tuesday, March 5<br>7:00pm</div>
  <div class="blurb" style="left:35px; top:1140px; width:663px; height:116px;">The British vocal ensemble CANTUS NINE is now established as one of the most versatile and bestloved singing groups in the world. Touring extensively throughout Europe, North America and<br>Asia, the ensemble performs a repertory from Renaissance polyphony to vocal jazz to<br>contemporary commissions and arrangements. Don't miss their fifth appearance on “Music at<br>St. Alder's”!<br>Tickets for Cantus Nine are $20 ($10 for students), and will go on sale February 1.</div>
</div>
</body>
</html>
```